Zielgruppe
Ich biete farbenzwerge, Glitzertattoos, Schwangerschaftsbemalung (Belly-Painting), Wunden schminken, Vermietung von einer Popcornmaschine.
Aufgabenstellung
Mein Anliegen betrifft hiermit die Gestaltung einer Website.
In Bezug auf die Website gibt es schon eine gekaufte Domain, welche lautet: tupfelzauber-atelier.de und kann über WEBRIX eingerichtet werden.
Auf dieser WEBSITE soll sich folgendes Menü befinden:
- Anfrage stellen/Angebot einholen mit zusätzlicher Frage 'Wie sind Sie auf mich aufmerksam geworden?'
Mit einem Feld für den Namen, E-Mail, Telefonnummer, Gewünschtes Datum.
Sowie die Frage 'Wie sind Sie auf mich aufmerksam geworden?' (zum Ankreuzen) Freunde, Empfehlung, Flyer, soziale medienoder sonstiges.
Gerne auch zum ankreuzen welche Leistung Sie möchten. farbenzwerge, Glitzer Tattoos, Schwangerschaftsbemalung, oder Popcornmaschiene. (So brauchen haben es die Kunden einfacher nur anzukreuzen und ich sehe gleich worum es sich handelt.)
- eine Leistungsübersicht: farbenzwerge, Glitzertattoos, Schwangerschaftsbemalung (Belly-Painting), Wunden schminken, Vermietung von einer Popcornmaschine
- meine Kontaktdaten
- Galerie (es kann eine Auswahl der angehängten Bilder sein)
!!! mein Wunsch wäre, dass sich die Figur von dem Logo in verschiedenen Positionen auf der Website an das Menü angepasst wiederfindet (wenn dies irgendwie machbar ist)
z.B. meine Figur (Logo) stehend am Rand oder liegend.....
- erwünscht ist auch eine Verknüpfung mit einem Suchfixeintrag
- Hinweis auf Plauderbook und Pixoramo (bin gerade dabei ein öffentliches Profil dort zu erstellen)
!Wichtig wäre die nötige Einstellung, damit die Website sowohl in der mobilen Version als auch der PC-Version mit ALLEN oben genannten Informationen dargestellt wird!
Dankbar wäre ich noch für die Information, ob für mich laufende Kosten (monatlich oder jährlich) für die Website entstehen?
Mein Logo ist mir sehr wichtig und sollte gut sichtbar und erkennbar sein auch die Schriftart kann auf der Website aufgegriffen werden

```html
<!DOCTYPE html>
<html lang="de">
<head>
<meta charset="utf-8">
<title>Tupfelzauber – farbenzwerge &amp; Glitzertattoos</title>
<link href="https://fonts.googleapis.com/css2?family=Amatic+SC:wght@400;700&family=Poppins:wght@400;500;600&display=swap" rel="stylesheet">
<style>
:root{
  --teal:#2ba3b4;
  --teal-deep:#3aaab9;
  --teal-pale:#eaf6f8;
  --teal-mid:#c3e6ec;
  --orange:#f08a4b;
  --button:#f2803e;
  --ink:#1a1a1a;
  --white:#ffffff;
  --photo-warm:#c9a98a;
  --photo-green:#6f8a4a;
  --photo-skin:#d9a899;
  --photo-dark:#3a3f48;
  --photo-red:#c9473f;
}
*{box-sizing:border-box;margin:0;padding:0}
html,body{width:1200px;height:5273px;overflow:hidden}
body{
  position:relative;
  font-family:'Poppins',sans-serif;
  color:var(--ink);
  background:linear-gradient(180deg,var(--white) 0px,var(--teal-pale) 1150px,var(--teal-mid) 3000px,var(--teal-deep) 4829px,var(--white) 4829px);
}
.abs{position:absolute}
.display{font-family:'Amatic SC',cursive;font-weight:400;line-height:1}

/* header */
.brand{left:41px;top:30px;width:360px;height:236px;display:flex;align-items:center;gap:18px}
.brand-name{font-family:'Amatic SC',cursive;font-weight:700;font-size:76px;color:var(--teal);line-height:1}
.brand-dot{width:26px;height:26px;border-radius:50%;background:var(--teal)}
.nav a{position:absolute;top:118px;font-family:'Amatic SC',cursive;font-size:62px;color:var(--teal);text-decoration:none;line-height:1}

/* sections */
.section-title{font-size:168px;color:var(--teal)}
.service-label{font-weight:600;font-size:33px;line-height:49px;text-align:center;color:var(--ink)}
.photo{display:block}

.gallery{left:43px;top:1376px;width:1110px;height:994px;display:grid;grid-template-columns:369px 364px 365px;grid-template-rows:318px 332px 336px;gap:4px 6px}

.reviews-title{left:0;width:1200px;top:2458px;text-align:center;font-size:168px;color:var(--white)}
.review{border:3px solid var(--orange);border-radius:8px;text-align:center;font-size:17px;line-height:28px;padding:12px 24px}
.stars{color:var(--white);font-size:22px;letter-spacing:2px;line-height:30px;margin-bottom:6px}
.palette{border-radius:50%;background:var(--white);border:3px solid var(--ink)}

.contact-title{left:0;width:1200px;text-align:center;color:var(--white);font-size:176px}
.field{left:254px;width:711px;height:49px;border:2px solid var(--white);border-radius:3px;color:var(--white);font-size:28px;line-height:45px;padding-left:10px}
.form-q{left:262px;color:var(--white);font-size:28px;line-height:40px}
.check{display:flex;align-items:center;gap:14px;color:var(--white);font-size:28px;line-height:40px}
.box{width:34px;height:34px;border:2px solid var(--white);border-radius:4px;flex:none}
.send{left:254px;top:4565px;width:711px;height:51px;background:var(--button);color:var(--white);font-size:28px;text-align:center;line-height:51px}

/* footer */
.foot-brand{left:41px;top:4874px;width:512px;height:338px;display:flex;align-items:center;gap:22px}
.foot-brand .brand-name{font-size:112px}
.foot-contact{right:18px;top:5030px;text-align:right;color:var(--teal);font-size:28px;line-height:41px}
.socials{right:18px;top:5190px;display:flex;gap:22px;color:var(--teal);font-size:28px;font-weight:500}
</style>
</head>
<body>

<header>
  <div class="abs brand"><span class="brand-dot"></span><span class="brand-name">Tupfelzauber</span></div>
  <nav class="nav">
    <a style="left:416px">Leistungen</a>
    <a style="left:651px">Galerie</a>
    <a style="left:827px">Referenzen</a>
    <a style="left:1061px">Kontakt</a>
  </nav>
</header>

<section>
  <h1 class="abs display section-title" style="left:72px;top:398px">Leistungen</h1>

  <div class="abs service-label" style="left:41px;top:672px;width:235px">Belly Painting</div>
  <div class="abs photo" role="img" aria-label="Foto: bemalter Babybauch mit Strohhut" style="left:63px;top:733px;width:214px;height:369px;background:linear-gradient(160deg,var(--photo-warm),#8c7a66)"></div>

  <div class="abs photo" role="img" aria-label="Foto: Glitzertattoos auf Unterarmen" style="left:295px;top:602px;width:207px;height:342px;background:linear-gradient(160deg,#cfa58a,#7d8a5c)"></div>
  <div class="abs service-label" style="left:280px;top:945px;width:240px">Glitzertattoos</div>

  <div class="abs service-label" style="left:516px;top:625px;width:226px">Farbenzwerge</div>
  <div class="abs photo" role="img" aria-label="Foto: Schminken eines Kindergesichts" style="left:526px;top:731px;width:207px;height:273px;background:linear-gradient(160deg,#b9b4ae,var(--photo-dark))"></div>

  <div class="abs photo" role="img" aria-label="Foto: Popcorntüten rot-weiß" style="left:752px;top:602px;width:198px;height:342px;background:linear-gradient(160deg,#e9b9b0,var(--photo-red))"></div>
  <div class="abs service-label" style="left:730px;top:945px;width:240px">Verleih<br>Popcorn<br>Maschine</div>

  <div class="abs service-label" style="left:978px;top:603px;width:224px">Wunden<br>Schminken</div>
  <div class="abs photo" role="img" aria-label="Foto: geschminkte Wunde im Gesicht" style="left:985px;top:729px;width:209px;height:373px;background:linear-gradient(160deg,#e6c2b5,#a6443c)"></div>
</section>

<section>
  <h2 class="abs display section-title" style="left:850px;top:1176px">Galerie</h2>
  <div class="abs gallery">
    <div role="img" aria-label="Foto: Belly Painting im Grünen" style="background:linear-gradient(160deg,var(--photo-green),var(--photo-warm))"></div>
    <div role="img" aria-label="Foto: Glitzertattoo wird aufgetragen" style="background:linear-gradient(160deg,#e2b8c0,#5a4d4a)"></div>
    <div role="img" aria-label="Foto: Bodypainting mit Fisch-Motiv" style="background:linear-gradient(160deg,#8a5a3c,#3e7fb8)"></div>
    <div role="img" aria-label="Foto: Gruppe mit Glitzertattoos" style="background:linear-gradient(160deg,#8c8a84,var(--photo-green))"></div>
    <div role="img" aria-label="Foto: Glitzertattoo am Arm" style="background:linear-gradient(160deg,#e5b6bf,#b86fa4)"></div>
    <div role="img" aria-label="Foto: bemalte Hand vor dunklem Hintergrund" style="background:linear-gradient(160deg,#25282e,#d8b29a)"></div>
    <div role="img" aria-label="Foto: Schmetterling wird ins Gesicht gemalt" style="background:linear-gradient(160deg,#d3b4a2,#4b5d8a)"></div>
    <div role="img" aria-label="Foto: Bodypainting am Rücken" style="background:linear-gradient(160deg,#6d5238,#3a8fb0)"></div>
    <div role="img" aria-label="Foto: Kindergesicht mit Bienen-Motiv" style="background:linear-gradient(160deg,#e7b28b,#d9672d)"></div>
  </div>
</section>

<section>
  <h2 class="abs display reviews-title">Referenzen</h2>
  <div class="abs review" style="left:78px;top:2648px;width:493px;height:115px"><div class="stars">★★★★★</div>Alles Bestens, würde ich wieder buchen!</div>
  <div class="abs review" style="left:602px;top:2648px;width:494px;height:115px"><div class="stars">★★★★★</div>Ich kann nichts sagen außer, super!</div>
  <div class="abs review" style="left:78px;top:2777px;width:489px;height:201px"><div class="stars">★★★★★</div>So freundlich zu den kleinen. Habe Sie zu einem Kindergeburtstag meiner Tochter gebucht und diese war begeistert. Wirklich zu empfehlen.</div>
  <div class="abs review" style="left:602px;top:2777px;width:489px;height:201px"><div class="stars">★★★★★</div>Die Kids sind super auf die Popcornmaschine abgefahren.<br>War der Hit der Feier!</div>
  <div class="abs palette" role="img" aria-label="Dekoration: Malerpalette" style="left:1044px;top:2601px;width:93px;height:92px"></div>
  <div class="abs palette" role="img" aria-label="Dekoration: Malerpalette" style="left:41px;top:2929px;width:96px;height:92px"></div>
</section>

<section>
  <h2 class="abs display contact-title" style="top:3160px">Interesse geweckt?</h2>
  <h2 class="abs display contact-title" style="top:3322px">Kontakt</h2>

  <div class="abs field" style="top:3478px">Name</div>
  <div class="abs field" style="top:3553px">E-Mail Adresse</div>
  <div class="abs field" style="top:3637px">Gewünschtes Datum</div>

  <div class="abs form-q" style="top:3712px">Welche Leistung wollen Sie in Anspruch nehmen?</div>
  <div class="abs check" style="left:254px;top:3763px"><span class="box"></span>Farbenzwerge</div>
  <div class="abs check" style="left:254px;top:3814px"><span class="box"></span>Glitzertattoos</div>
  <div class="abs check" style="left:254px;top:3867px"><span class="box"></span>Popcornmaschine mieten</div>
  <div class="abs check" style="left:254px;top:3926px"><span class="box"></span>Sonstiges</div>

  <div class="abs form-q" style="top:3982px">Wie sind Sie auf mich aufmerksam geworden?</div>
  <div class="abs check" style="left:254px;top:4033px"><span class="box"></span>Freunde</div>
  <div class="abs check" style="left:456px;top:4033px"><span class="box"></span>Sozial Media</div>
  <div class="abs check" style="left:707px;top:4033px"><span class="box"></span>Empfehlung</div>
  <div class="abs check" style="left:254px;top:4090px"><span class="box"></span>Sonstiges</div>

  <div class="abs field" style="top:4172px;height:358px">Ihre Nachricht</div>
  <div class="abs send">Absenden</div>
</section>

<footer>
  <div class="abs foot-brand"><span class="brand-dot"></span><span class="brand-name">Tupfelzauber</span></div>
  <div class="abs foot-contact">Lena Beispielfeld<br>Telefon: 0431 987654321<br>Email: post@beispielpost.de</div>
  <div class="abs socials"><span>Plauderbook</span><span>Pixoramo</span></div>
</footer>

</body>
</html>
```